Redesign responsive website and logo for webshop platform

Redesign our applications old website with a new clean, crisp modern looking style that is responsive.

Our application is a cloud based, free ecommerce platform that lets users set up their own webshops within minutes. (Similar to Mabrook https://mabrook.example/l/sell)

Our old website: http://sv.vendlyx.example/

I need redesigned HTML + CSS for the following three pages:
* Landing Page:
(Old page: http://sv.vendlyx.example/)
I have attached a mockup of a proposed layout/structure for the landing page.
- Pricing comparision/features page
(Old page http://sv.vendlyx.example/t/funktioner)
- Generic "article" page:
(Old page http://sv.vendlyx.example/d/redigerasida)

The pages must responsive using HTML 5/CSS 3 (I prefer Bootstrap 3 if possible).

I also need a redesign of the logotype.

If you have any questions don't hesitate to ask and we will provide whatever is needed to you.

Logo Text

Vendlyx

Coding

Coded - Design and coding required

Number of Pages Required

3 page

Font styles to use
Serif
Sans Serif

```html
<!DOCTYPE html>
<html lang="sv">
<head>
<meta charset="utf-8">
<title>Vendlyx – Starta en gratis webshop</title>
<link rel="stylesheet" href="https://fonts.googleapis.com/css2?family=Lato:ital,wght@0,400;0,700;1,400;1,700&display=swap">
<style>
:root{
  --blue:#1b5aa6;
  --sky:#1797d4;
  --ink:#1e1e1e;
  --muted:#444;
  --grey-bg:#efefef;
  --line:#d6d6d6;
  --hero-dark:#1c1d1f;
  --footer:#0d0d0d;
  --soft:#dcdcdc;
}
*{box-sizing:border-box;margin:0;padding:0}
html,body{width:764px;height:1200px;overflow:hidden}
body{position:relative;font-family:"Lato",Arial,sans-serif;color:var(--ink);background:#fff}
.abs{position:absolute}

/* header */
.site-header{position:absolute;left:0;top:0;width:764px;height:53px;background:#fff;border-top:2px solid var(--blue)}
.contact{position:absolute;top:18px;display:flex;align-items:center;gap:8px;font-size:8px;font-style:italic;color:#333}
.contact .dot{width:18px;height:18px;border-radius:50%;border:2px solid var(--soft);display:flex;align-items:center;justify-content:center}
.brand{position:absolute;left:310px;top:6px;width:144px;text-align:center}
.brand-name{display:flex;align-items:center;justify-content:center;gap:6px;font-size:29px;font-weight:700;color:var(--blue);line-height:30px}
.brand-name .mark{width:22px;height:22px;border-radius:50%;background:var(--blue)}
.brand-tag{font-size:5.5px;color:#333;letter-spacing:.3px;margin-left:28px;margin-top:-1px}

/* hero */
.hero{position:absolute;left:0;top:53px;width:764px;height:348px;background:radial-gradient(ellipse at 60% 45%,#3a3b3d 0%,#26272a 45%,var(--hero-dark) 100%)}
.hero-title{position:absolute;left:0;top:115px;width:764px;text-align:center;color:#fff;font-style:italic;font-weight:700;font-size:24px;line-height:29px}
.signup{position:absolute;left:134px;top:189px;width:496px;height:38px;background:rgba(0,0,0,.55);border-radius:2px}
.field{position:absolute;top:7px;height:24px;width:146px;background:#fff;border-radius:2px;font-size:7px;font-style:italic;color:#888;padding:7px 9px}
.btn{position:absolute;border-radius:2px;color:#fff;font-style:italic;font-weight:700;font-size:7.5px;text-align:center}
.btn-primary{left:308px;top:7px;width:104px;height:24px;background:var(--blue);line-height:24px}
.btn-login{left:441px;top:6px;width:47px;height:24px;background:var(--sky);line-height:24px}
.or{position:absolute;left:421px;top:14px;font-size:8px;font-style:italic;color:#fff}
.pager span{position:absolute;top:322px;width:6px;height:6px;border-radius:50%;background:#fff}
.pager .active{width:8px;height:8px;top:321px;background:var(--blue);border:1px solid #fff}

/* intro */
.section-title{position:absolute;left:0;width:764px;text-align:center;font-size:17px;font-weight:700;font-style:italic;color:var(--ink)}
.section-title em{color:var(--blue)}
.section-mark{position:absolute;left:377px;width:10px;height:10px;border-radius:50%;border:1.5px solid #c8c8c8}
.lead{position:absolute;left:150px;width:464px;text-align:center;font-size:7.2px;line-height:13px;color:#222}

/* features */
.features{position:absolute;left:0;top:533px;width:764px;height:469px;background:var(--grey-bg)}
.feature{position:absolute;width:270px}
.feature h3{position:absolute;left:48px;top:0;font-size:12px;font-weight:400;letter-spacing:.2px;color:#222;white-space:nowrap}
.feature p{position:absolute;left:48px;top:20px;width:215px;font-size:6.6px;line-height:13.6px;color:#333}
.feature svg{position:absolute;left:0;top:-3px}
.rule-h{position:absolute;height:0;border-top:1px dotted var(--line)}
.rule-v{position:absolute;width:0;border-left:1px dotted var(--line)}
.btn-start{left:349px;top:417px;width:66px;height:24px;line-height:24px;background:var(--sky)}

/* services */
.service{position:absolute;top:1034px;width:130px;text-align:center;font-size:9px;color:#222;line-height:12px}
.service .ring{width:72px;height:72px;margin:0 auto 13px;border-radius:50%;background:#e2e2e2;display:flex;align-items:center;justify-content:center}
.service .ring span{width:48px;height:48px;border-radius:50%;background:#fff;display:flex;align-items:center;justify-content:center}

/* footer */
.site-footer{position:absolute;left:0;top:1171px;width:764px;height:29px;background:var(--footer)}
.social{position:absolute;top:8px;width:14px;height:14px;border-radius:50%;background:#fff}
.copy{position:absolute;left:0;top:10px;width:764px;text-align:center;font-size:7px;font-style:italic;color:#ddd}
.footer-brand{position:absolute;left:584px;top:4px;display:flex;align-items:center;gap:4px;font-size:18px;font-weight:700;color:#fff}
.footer-brand .mark{width:14px;height:14px;border-radius:50%;background:#fff}
</style>
</head>
<body>

<header class="site-header">
  <div class="contact" style="left:105px">
    <span class="dot"><svg width="8" height="6" viewBox="0 0 8 6"><rect width="8" height="6" rx="1" fill="#1b5aa6"/><path d="M0 0l4 3 4-3" stroke="#fff" stroke-width=".8" fill="none"/></svg></span>
    info@vendlyx.example
  </div>
  <div class="brand">
    <div class="brand-name"><span class="mark"></span>Vendlyx</div>
    <div class="brand-tag">set up your own stores within minutes</div>
  </div>
  <div class="contact" style="left:574px">
    <span class="dot"><svg width="8" height="8" viewBox="0 0 8 8"><circle cx="4" cy="4" r="3" fill="#1b5aa6"/></svg></span>
    Vendlyx på Chirpline
  </div>
</header>

<section class="hero" role="img" aria-label="Dimmed photo of a person working at a laptop in a café">
  <svg class="abs" style="left:40px;top:150px" width="25" height="48" viewBox="0 0 25 48"><path d="M24 1L1 24l23 23" stroke="#fff" stroke-width="1.2" fill="none"/></svg>
  <svg class="abs" style="left:700px;top:150px" width="25" height="48" viewBox="0 0 25 48"><path d="M1 1l23 23L1 47" stroke="#fff" stroke-width="1.2" fill="none"/></svg>
  <h1 class="hero-title">Lets's Start set up Your<br>own stores within minutes.</h1>
  <form class="signup">
    <div class="field" style="left:7px">Your Email</div>
    <div class="field" style="left:157px;padding-left:24px">Your Password</div>
    <div class="btn btn-primary">Skapa en webshop</div>
    <span class="or">Or</span>
    <div class="btn btn-login">Login</div>
  </form>
  <div class="pager"><span style="left:367px"></span><span class="active" style="left:377px"></span><span style="left:390px"></span></div>
</section>

<section class="intro">
  <h2 class="section-title" style="top:431px">Starta en <em>Gratis Webshop</em></h2>
  <span class="section-mark" style="top:462px"></span>
  <p class="lead" style="top:481px">Vendlyx är en tjänst som låter dig starta en komplett internetbutik. Tjänsten är gratis och har allt som krävs för att du ska komma igång med din verksamhet och sälja produkter online.</p>
</section>

<section class="features">
  <h2 class="section-title" style="top:24px">Our <em>feature</em></h2>
  <span class="section-mark" style="top:56px"></span>
  <p class="lead" style="top:75px">Vendlyx är en tjänst som låter dig starta en komplett internetbutik. Tjänsten är gratis och har allt som krävs för att du ska komma igång med din verksamhet och sälja produkter online.</p>

  <div class="rule-v" style="left:382px;top:128px;height:255px"></div>
  <div class="rule-h" style="left:110px;top:209px;width:258px"></div>
  <div class="rule-h" style="left:396px;top:209px;width:258px"></div>
  <div class="rule-h" style="left:110px;top:304px;width:258px"></div>
  <div class="rule-h" style="left:396px;top:304px;width:258px"></div>

  <div class="feature" style="left:102px;top:141px">
    <svg width="32" height="40" viewBox="0 0 32 40"><path d="M4 14a12 12 0 0 1 24 0" stroke="#1797d4" stroke-width="2.5" fill="none"/><path d="M9 14a7 7 0 0 1 14 0" stroke="#1797d4" stroke-width="2.5" fill="none"/><path d="M14 12h4v12h6a3 3 0 0 1 3 3v7a5 5 0 0 1-5 5h-8l-5-9 2-2 3 3z" fill="#1b5aa6"/></svg>
    <h3>KOM IGÅNG PÅ 5 MINUTER</h3>
    <p>Att starta en ebutik med Vendlyx tar inte mer än 5 minuter.Skapa ett konto för att komma igång. Ingenting behöver installeras på din dator.</p>
  </div>
  <div class="feature" style="left:402px;top:141px">
    <svg width="32" height="34" viewBox="0 0 32 34"><rect x="1" y="2" width="30" height="22" rx="2" stroke="#1b5aa6" stroke-width="2" fill="none"/><path d="M8 8h3l2 8h9l2-6H12" stroke="#1b5aa6" stroke-width="1.6" fill="none"/><circle cx="14" cy="19" r="1.3" fill="#1b5aa6"/><circle cx="21" cy="19" r="1.3" fill="#1b5aa6"/><path d="M12 24v4M20 24v4M7 30h18" stroke="#1b5aa6" stroke-width="2"/></svg>
    <h3>SKAPA EN GRATIS WEBBUTIK</h3>
    <p>Att starta en ebutik med Vendlyx tar inte mer än 5 minuter.Skapa ett konto för att komma igång. Ingenting behöver installeras på din dator.</p>
  </div>
  <div class="feature" style="left:102px;top:233px">
    <svg width="32" height="36" viewBox="0 0 32 36"><circle cx="8" cy="8" r="4.5" fill="#1b5aa6"/><path d="M1 34V20a6 6 0 0 1 6-6h3a6 6 0 0 1 6 6v14z" fill="#1b5aa6"/><rect x="18" y="12" width="12" height="16" stroke="#1797d4" stroke-width="1.8" fill="#fff"/><path d="M21 17h6M21 21h6M21 25h4" stroke="#1797d4" stroke-width="1.4"/><circle cx="25" cy="6" r="3.5" stroke="#1b5aa6" stroke-width="1.5" fill="none"/></svg>
    <h3>INTUITIVT ANVÄNDARGRÄNSSNITT</h3>
    <p>Att starta en ebutik med Vendlyx tar inte mer än 5 minuter.Skapa ett konto för att komma igång. Ingenting behöver installeras på din dator.</p>
  </div>
  <div class="feature" style="left:402px;top:233px">
    <svg width="34" height="36" viewBox="0 0 34 36"><circle cx="12" cy="12" r="9" stroke="#1b5aa6" stroke-width="3" fill="none"/><path d="M18 19l12 13" stroke="#1b5aa6" stroke-width="4.5" stroke-linecap="round"/><circle cx="24" cy="8" r="4" stroke="#1797d4" stroke-width="2" fill="none"/></svg>
    <h3>SÖKMOTOROPTIMERAD</h3>
    <p>Att starta en ebutik med Vendlyx tar inte mer än 5 minuter.Skapa ett konto för att komma igång. Ingenting behöver installeras på din dator.</p>
  </div>
  <div class="feature" style="left:102px;top:330px">
    <svg width="32" height="30" viewBox="0 0 32 30"><path d="M3 2h26l2 7H1z" fill="#1797d4"/><path d="M1 9h30v3H1z" fill="#1b5aa6"/><rect x="3" y="12" width="26" height="16" stroke="#1b5aa6" stroke-width="2" fill="none"/><rect x="6" y="16" width="6" height="12" stroke="#1b5aa6" stroke-width="1.6" fill="none"/><rect x="15" y="16" width="11" height="8" stroke="#1797d4" stroke-width="1.6" fill="none"/></svg>
    <h3>DESIGNA DIN WEBSHOP</h3>
    <p>Att starta en ebutik med Vendlyx tar inte mer än 5 minuter.Skapa ett konto för att komma igång. Ingenting behöver installeras på din dator.</p>
  </div>
  <div class="feature" style="left:402px;top:330px">
    <svg width="32" height="30" viewBox="0 0 32 30"><rect x="2" y="2" width="28" height="20" stroke="#1b5aa6" stroke-width="2" fill="none"/><path d="M6 17l6-7 5 5 4-6 5 8" stroke="#1797d4" stroke-width="1.6" fill="none"/><path d="M16 22v4M10 28h12" stroke="#1b5aa6" stroke-width="2"/></svg>
    <h3>SMART DASHBOARD</h3>
    <p>Att starta en ebutik med Vendlyx tar inte mer än 5 minuter.Skapa ett konto för att komma igång. Ingenting behöver installeras på din dator.</p>
  </div>

  <a class="btn btn-start">Start Now</a>
</section>

<section class="services">
  <svg class="abs" style="left:74px;top:1071px" width="10" height="14" viewBox="0 0 10 14"><path d="M8 1L2 7l6 6" stroke="#222" stroke-width="2.4" fill="none"/></svg>
  <svg class="abs" style="left:684px;top:1071px" width="10" height="14" viewBox="0 0 10 14"><path d="M2 1l6 6-6 6" stroke="#c8c8c8" stroke-width="2" fill="none"/></svg>

  <div class="service" style="left:87px">
    <div class="ring"><span><svg width="24" height="22" viewBox="0 0 24 22"><circle cx="8" cy="13" r="6" stroke="#222" stroke-width="3" stroke-dasharray="2.5 1.5" fill="none"/><circle cx="8" cy="13" r="2" fill="#222"/><circle cx="18" cy="6" r="4" stroke="#222" stroke-width="2.4" stroke-dasharray="2 1.2" fill="none"/></svg></span></div>
    Product Management
  </div>
  <div class="service" style="left:240px">
    <div class="ring"><span><svg width="24" height="22" viewBox="0 0 24 22"><rect x="3" y="2" width="18" height="14" stroke="#222" stroke-width="1.8" fill="none"/><path d="M1 19h22" stroke="#222" stroke-width="2"/><path d="M8 13l8-8" stroke="#222" stroke-width="2"/></svg></span></div>
    Clean Design
  </div>
  <div class="service" style="left:393px">
    <div class="ring"><span><svg width="26" height="22" viewBox="0 0 26 22"><rect x="1" y="3" width="18" height="13" rx="1.5" stroke="#222" stroke-width="1.8" fill="none"/><path d="M1 7h18" stroke="#222" stroke-width="2"/><rect x="16" y="13" width="8" height="7" fill="#222"/><path d="M17.5 13v-2a2.5 2.5 0 0 1 5 0v2" stroke="#222" stroke-width="1.4" fill="none"/></svg></span></div>
    Safe &amp; Secure online<br>payment System
  </div>
  <div class="service" style="left:546px">
    <div class="ring"><span><svg width="26" height="26" viewBox="0 0 26 26"><circle cx="13" cy="13" r="10" stroke="#222" stroke-width="2" fill="none"/><text x="13" y="16.5" text-anchor="middle" font-family="Lato,Arial,sans-serif" font-size="9" font-weight="700" fill="#222">24</text></svg></span></div>
    24X7 Support
  </div>
</section>

<footer class="site-footer">
  <span class="social" style="left:103px"></span>
  <span class="social" style="left:122px"></span>
  <span class="social" style="left:142px"></span>
  <span class="social" style="left:161px"></span>
  <span class="social" style="left:180px"></span>
  <p class="copy">© Copyright 2016 Vendlyx. All Right reserved</p>
  <div class="footer-brand"><span class="mark"></span>Vendlyx</div>
</footer>

</body>
</html>
```